Graniteway Surface Works, Inc. Business Card

New business, we do epoxy, polishing concrete, underlayment, fluid applied flooring, sound proofing, double sided, will need 3 sets of cards with 3 different names and phone numbers.
Company: Graniteway Surface Works, Inc.
Address and Phone: 6339 Charlotte Pike PMB 2183Nashville, TN 38514
(615) 418-3927
www.granitewaysurfaceworks.example

Target Market(s)

General Contractors, Contractors, Architects

Contact Information for Business Card

1st Card: Devon Halvorsen C. 708.214.5873 e. devon@granitewaysurfaceworks.example
Vice President
2nd Card: Morgan Prescoe C. 708.389.6145 e. morgan@granitewaysurfaceworks.example
President
3rd Card: Bo Vu C. 405.631.8207 e. bo@granitewaysurfaceworks.example
Managing Partner

Font styles to use
Serif
Sans Serif

Requirements
Must have
• Professional Clean Design, Implement colors from Logo or nicely contrasting
Nice to have
• N/A

```html
<!DOCTYPE html>
<html lang="en">
<head>
<meta charset="utf-8">
<title>Graniteway Surface Works, Inc. Business Card</title>
<link rel="stylesheet" href="https://fonts.googleapis.com/css2?family=Montserrat:wght@500;700&family=Arimo:wght@400&display=swap">
<style>
  :root {
    --backdrop: #262626;
    --card: #0c0c0c;
    --brand-blue: #1d6fc4;
    --silver: #c9c9c9;
    --text-light: #d4d4d4;
    --text-muted: #a9a9a9;
    --divider: #3a3a3a;
  }
  * { margin: 0; padding: 0; box-sizing: border-box; }
  html, body { width: 1200px; height: 900px; overflow: hidden; }
  body {
    background: var(--backdrop);
    display: flex;
    align-items: center;
    justify-content: center;
    gap: 30px;
    font-family: "Arimo", Arial, sans-serif;
  }
  .card {
    width: 560px;
    height: 320px;
    background: var(--card);
    border-radius: 20px;
    position: relative;
    overflow: hidden;
  }
  .card-front { display: flex; align-items: center; }
  .brand-block {
    width: 240px;
    flex: none;
    display: flex;
    flex-direction: column;
    align-items: center;
    gap: 14px;
  }
  .brand-square {
    width: 56px; height: 56px;
    background: var(--brand-blue);
  }
  .brand-name {
    font-family: "Montserrat", Arial, sans-serif;
    font-weight: 500;
    font-size: 15px;
    letter-spacing: 1.5px;
    text-transform: uppercase;
    color: var(--text-light);
    text-align: center;
    line-height: 1.5;
  }
  .divider {
    width: 1px; height: 190px;
    flex: none;
    background: var(--divider);
  }
  .contact-block { padding: 0 20px 0 24px; min-width: 0; }
  .person-name {
    font-family: "Montserrat", Arial, sans-serif;
    font-weight: 700;
    font-size: 19px;
    color: var(--brand-blue);
    text-transform: uppercase;
    letter-spacing: 0.3px;
  }
  .person-title {
    font-size: 14px;
    color: var(--text-muted);
    margin: 2px 0 12px 6px;
  }
  .contact-list { list-style: none; margin-left: 6px; }
  .contact-list li {
    display: flex;
    align-items: center;
    gap: 9px;
    font-size: 12px;
    color: var(--text-light);
    line-height: 20px;
    white-space: nowrap;
  }
  .contact-list svg { width: 13px; height: 13px; flex: none; }
  .address {
    margin: 14px 0 0 6px;
    font-size: 13px;
    color: var(--text-muted);
    line-height: 18px;
  }
  .card-back {
    display: flex;
    flex-direction: column;
    align-items: center;
    justify-content: center;
    gap: 20px;
  }
  .card-back .brand-square { width: 72px; height: 72px; background: var(--silver); }
  .card-back .brand-name { font-size: 19px; color: var(--silver); }
</style>
</head>
<body>
  <section class="card card-front" aria-label="Business card front">
    <div class="brand-block">
      <div class="brand-square"></div>
      <div class="brand-name">Graniteway<br>Surface Works</div>
    </div>
    <div class="divider"></div>
    <div class="contact-block">
      <h1 class="person-name">Devon Halvorsen</h1>
      <p class="person-title">Vice President</p>
      <ul class="contact-list">
        <li>
          <svg viewBox="0 0 14 14" fill="none" stroke="var(--brand-blue)" stroke-width="1.5"><rect x="3.5" y="1" width="7" height="12" rx="1.2"/><line x1="6" y1="11" x2="8" y2="11"/></svg>
          708.214.5873
        </li>
        <li>
          <svg viewBox="0 0 14 14" fill="var(--brand-blue)"><path d="M3 1.2l2.2 2.6-1.1 1.5c.8 1.8 2.2 3.2 4 4l1.5-1.1 2.6 2.2-1.3 2.1C6 12.3 1.7 8 1 3z"/></svg>
          (615) 418-3927
        </li>
        <li>
          <svg viewBox="0 0 14 14" fill="var(--brand-blue)"><path d="M1 3h12v8H1z"/><path d="M1 3l6 4.5L13 3" fill="none" stroke="var(--card)" stroke-width="1.2"/></svg>
          devon@granitewaysurfaceworks.example
        </li>
        <li>
          <svg viewBox="0 0 14 14" fill="none" stroke="var(--brand-blue)" stroke-width="1.2"><circle cx="7" cy="7" r="5.8"/><ellipse cx="7" cy="7" rx="2.6" ry="5.8"/><line x1="1.2" y1="7" x2="12.8" y2="7"/></svg>
          www.granitewaysurfaceworks.example
        </li>
      </ul>
      <p class="address">4812 Wendover Ridge<br>PMB 7416, Nashville, TN 38514</p>
    </div>
  </section>

  <section class="card card-back" aria-label="Business card back">
    <div class="brand-square"></div>
    <div class="brand-name">Graniteway Surface Works</div>
  </section>
</body>
</html>
```